Bold Website Design for Fitness Trainer - No Coding

We are in need of a bold and unique website design for a personal fitness training company, www.TessaRowle.com. We need DESIGN ONLY for three pages. These will be a homepage, a lead capture page, and one internal page with a sidebar. The design will be used for coding a wordpress theme, if that matters for the designer.

Tessa Rowle Fitness Training
2718 E 57th St #193
Austin, TX 78705
512-460-7198
http://www.tessarowle.com

Target Market(s)

18-45 year old male and females making 80k+ a year and looking to get stronger and in shape.

Industry/Entity Type

Fitness

Number of Pages Required

3 page

Font styles to use
Sans Serif

Requirements
Must have
• See attached design specs file.
Nice to have
Should not have
• Boxed layout.
• Dark Background.

```html
<!DOCTYPE html>
<html lang="en">
<head>
<meta charset="utf-8">
<title>Tessa Rowle Fitness Training</title>
<link rel="stylesheet" href="https://fonts.googleapis.com/css2?family=Open+Sans:wght@400;600;700;800&display=swap">
<style>
:root{
  --pink:#ec2a8e;
  --pink-dark:#c81c74;
  --yellow:#f7d417;
  --ink:#333333;
  --muted:#666666;
  --line:#e3e3e3;
  --chirp:#2aa3e0;
  --friend:#3c5a99;
  --snap:#517fa4;
  --footer:#2b2b2b;
}
*{box-sizing:border-box;margin:0;padding:0}
html,body{width:1200px;height:2821px;overflow:hidden}
body{font-family:"Open Sans",Arial,sans-serif;color:var(--ink);background:#fff;position:relative}
.abs{position:absolute}
.btn{position:absolute;display:flex;align-items:center;justify-content:center;font-weight:700;font-size:10px;text-transform:uppercase;border-radius:3px}
.btn-yellow{background:var(--yellow);color:#222}
.btn-pink{background:var(--pink);color:#fff}

/* top bar */
.topbar{position:absolute;left:0;top:0;width:1200px;height:38px;background:var(--pink);color:#fff;font-size:12px}
.topbar .phone{position:absolute;left:165px;top:11px;display:flex;align-items:center;gap:10px}
.nav{position:absolute;top:0;left:749px;display:flex;height:38px}
.nav a{color:#fff;text-decoration:none;font-size:10px;font-weight:600;display:flex;align-items:center;padding:0 14px;height:38px}
.nav a.active{background:var(--pink-dark)}

/* hero */
.hero{position:absolute;left:0;top:38px;width:1200px;height:487px;overflow:hidden}
.hero-photo{position:absolute;inset:0;background:linear-gradient(120deg,#4a5a66 0%,#8d9aa2 35%,#b9c3c8 60%,#7e8c96 100%)}
.hero-shade{position:absolute;inset:0;background:rgba(20,25,30,.35)}
.hero-head{position:absolute;left:0;top:0;width:1200px;height:105px;background:rgba(0,0,0,.35)}
.brand{position:absolute;left:165px;top:22px;display:flex;align-items:center;gap:10px}
.brand .mark{width:50px;height:50px;border-radius:50%;background:var(--yellow)}
.brand .name{font-size:28px;font-weight:800;color:#fff}
.hero-copy{position:absolute;left:0;width:1200px;text-align:center;color:#fff}
.hero-copy .hello{top:196px;font-size:17px;font-weight:700}
.hero-copy .title-pink{top:222px;font-size:44px;font-weight:800;color:var(--pink);line-height:1}
.hero-copy .title-white{top:270px;font-size:44px;font-weight:800;line-height:1}
.hero-copy .tag{top:328px;font-size:17px;font-weight:600}
.slider-dots{position:absolute;left:541px;top:448px;display:flex;gap:3px}
.slider-dots i{display:block;width:38px;height:5px;background:#fff}
.slider-dots i.on{background:var(--pink)}

/* about */
.about{position:absolute;left:0;top:525px;width:1200px;height:415px;background:linear-gradient(180deg,#f4f4f4,#d9d9d9)}
.about-photo{position:absolute;left:160px;top:30px;width:405px;height:385px;background:linear-gradient(180deg,#c99a7e,#2c2f36 60%,#33363d)}
.about .kicker{position:absolute;left:611px;top:140px;font-size:12px;font-weight:600}
.about h2{position:absolute;left:611px;top:153px;font-size:30px;font-weight:700;letter-spacing:.5px}
.about p{position:absolute;left:611px;top:197px;width:433px;font-size:10px;line-height:15px;color:#444}

/* section titles */
.sec-title{position:absolute;left:0;width:1200px;text-align:center;font-size:19px;font-weight:700;color:#444}
.sec-sub{position:absolute;left:280px;width:640px;text-align:center;font-size:12px;line-height:19px;color:#666}

/* services */
.service{position:absolute;top:1123px;width:277px;height:203px;border:1px solid var(--line);box-shadow:0 1px 4px rgba(0,0,0,.08);background:#fff;text-align:center}
.service .icon{position:absolute;left:100px;top:-48px;width:76px;height:76px;border-radius:50%;background:#fff;border:2px solid var(--pink);display:flex;align-items:center;justify-content:center}
.service .icon span{width:64px;height:64px;border-radius:50%;background:var(--pink);display:flex;align-items:center;justify-content:center}
.service h3{margin-top:50px;font-size:13px;font-weight:700}
.service h3.pink{color:var(--pink)}
.service p{margin:12px auto 0;width:240px;font-size:9.5px;line-height:15px;color:#555}
.service .btn{left:93px;top:146px;width:92px;height:32px}

/* stories */
.stories{position:absolute;left:0;top:1373px;width:1200px;height:297px;background:repeating-linear-gradient(90deg,#e6e6e6 0 40px,#d2d2d2 40px 80px,#efefef 80px 120px)}
.story-card{position:absolute;left:312px;top:32px;width:576px;height:224px;background:#fff;box-shadow:0 2px 8px rgba(0,0,0,.2)}
.story-card h3{position:absolute;left:0;width:576px;top:26px;text-align:center;font-size:16px;font-weight:700;color:#444}
.story-card .avatar{position:absolute;left:30px;top:72px;width:68px;height:68px;border-radius:50%;border:3px solid var(--pink);background:linear-gradient(#9aa3ad,#4a4f58)}
.story-card blockquote{position:absolute;left:125px;top:86px;width:420px;font-size:10.5px;line-height:17px;color:#555}
.story-card blockquote b{color:var(--pink);font-size:20px;line-height:0}
.story-card .who{position:absolute;left:125px;top:150px;font-size:11px;font-weight:700}
.dots{position:absolute;left:272px;top:188px;display:flex;gap:3px}
.dots i{width:6px;height:6px;border-radius:50%;background:#ccc}
.dots i.on{background:var(--pink)}

/* social */
.social{position:absolute;top:1768px;width:277px;height:260px;border:1px solid var(--line);background:#fff;box-shadow:0 1px 4px rgba(0,0,0,.08)}
.social .head{height:38px;color:#fff;font-size:11px;font-weight:600;display:flex;align-items:center;gap:10px;padding-left:20px;text-transform:uppercase}
.social .head i{width:14px;height:14px;background:rgba(255,255,255,.85);border-radius:2px}
.chirp .head{background:var(--chirp)}
.friend .head{background:var(--friend)}
.snap .head{background:var(--snap)}
.chirp .pic{position:absolute;left:20px;top:52px;width:40px;height:40px;border-radius:50%;border:2px solid var(--pink);background:#ddd}
.chirp .handle{position:absolute;left:72px;top:56px;font-size:12px;font-weight:600}
.chirp .rule{position:absolute;left:72px;top:80px;width:180px;height:2px;background:#eee}
.chirp p{position:absolute;left:20px;top:105px;width:240px;font-size:10px;line-height:16px;color:#555}
.chirp p span{color:var(--chirp);font-weight:600}
.chirp .foot{position:absolute;left:0;bottom:0;width:277px;height:38px;border-top:1px solid var(--line);font-size:9px;color:#888;display:flex;align-items:center;justify-content:space-between;padding:0 20px}
.chirp .foot u{color:var(--chirp);text-decoration:underline}
.friend .page{position:absolute;left:22px;top:50px;width:26px;height:26px;background:#d8c3b5}
.friend .pname{position:absolute;left:60px;top:50px;font-size:10px;font-weight:600;color:var(--friend)}
.friend .like{position:absolute;left:60px;top:66px;width:40px;height:14px;background:var(--friend);border-radius:2px}
.friend .grid{position:absolute;left:22px;top:100px;display:grid;grid-template-columns:repeat(5,36px);gap:5px}
.friend .grid i{height:36px;background:#b7aca6}
.friend .grid i:nth-child(odd){background:#6f6660}
.friend .foot{position:absolute;left:22px;bottom:14px;font-size:9px;color:#555}
.snap .photo{position:absolute;left:20px;top:50px;width:237px;height:180px;border:1px solid var(--line);background:linear-gradient(90deg,#d9cfc8,#a88a78 50%,#ded6d0)}
.snap .foot{position:absolute;left:20px;bottom:6px;width:237px;display:flex;justify-content:space-between;font-size:9px;color:#555}

/* blog */
.post{position:absolute;top:2116px;width:277px}
.post .img{height:156px}
.post h4{margin-top:12px;font-size:10px;font-weight:700;line-height:15px}
.post p{margin-top:8px;font-size:9.5px;line-height:15px;color:#555}
.post a{display:block;margin-top:6px;font-size:9px;font-weight:700;color:var(--pink)}

/* cta */
.cta{position:absolute;left:0;top:2434px;width:1200px;height:149px;background:var(--pink);text-align:center;color:#fff}
.cta h2{margin-top:38px;font-size:23px;font-weight:700}
.cta .sub{margin-top:2px;font-size:13px}
.cta .btn{left:498px;top:102px;width:204px;height:33px}

/* footer */
.footer{position:absolute;left:0;top:2583px;width:1200px;height:238px;background:var(--footer);color:#fff;text-align:center}
.footer .stay{position:absolute;left:0;width:1200px;top:46px;font-size:12px}
.footer .nets{position:absolute;left:454px;top:94px;display:flex;gap:34px}
.footer .net{width:50px;text-align:center;font-size:9px;font-weight:600}
.footer .net i{display:block;margin:0 auto 10px;width:40px;height:40px;border-radius:50%;background:#4d4d4d}
.footer .net.on i{background:var(--pink)}
.footer .rule{position:absolute;left:520px;top:186px;width:160px;height:1px;background:#444}
.footer .copy{position:absolute;left:0;width:1200px;top:194px;font-size:9px;color:#bbb;line-height:16px}
.footer .copy b{color:#fff}
</style>
</head>
<body>

<header class="topbar">
  <div class="phone">
    <svg width="14" height="14" viewBox="0 0 24 24"><circle cx="12" cy="12" r="12" fill="#fff" opacity=".25"/><path d="M8 6l2 3-1.5 1.5a8 8 0 004 4L14 13l3 2-1.5 2.5C10 17 7 14 6.5 8.5z" fill="#fff"/></svg>
    Call US : 009-412-870
  </div>
  <nav class="nav">
    <a class="active">HOME</a><a>SERVICES</a><a>LEAD CAPTURE</a><a>CONTACT US</a>
  </nav>
</header>

<section class="hero">
  <div class="hero-photo" role="img" aria-label="Woman training on a pull-up machine in a gym"></div>
  <div class="hero-shade"></div>
  <div class="hero-head"></div>
  <div class="brand"><span class="mark"></span><span class="name">Tessa Rowle</span></div>
  <div class="btn btn-yellow" style="left:910px;top:18px;width:128px;height:36px">Get a free session</div>
  <svg class="abs" style="left:110px;top:230px" width="16" height="30" viewBox="0 0 16 30"><path d="M13 2L3 15l10 13" stroke="#fff" stroke-width="2.5" fill="none"/></svg>
  <svg class="abs" style="left:1078px;top:230px" width="16" height="30" viewBox="0 0 16 30"><path d="M3 2l10 13L3 28" stroke="#fff" stroke-width="2.5" fill="none"/></svg>
  <div class="hero-copy abs hello" style="top:196px">HELLO! I AM TESSA ROWLE</div>
  <div class="hero-copy abs title-pink" style="top:222px">TESSA ROWLE</div>
  <div class="hero-copy abs title-white" style="top:270px">FITNESS TRAINING</div>
  <div class="hero-copy abs tag" style="top:328px">HELPS YOU GET MORE ACTIVE</div>
  <div class="slider-dots"><i class="on"></i><i></i><i></i></div>
</section>

<section class="about">
  <div class="about-photo" role="img" aria-label="Trainer in a black tank top flexing her arm in front of a city skyline"></div>
  <div class="kicker">WANT TO KNOW</div>
  <h2>ABOUT ME</h2>
  <p>Sed ut perspiciatis unde omnis iste natus error sit voluptatem accusantium doloremque laudantium, totam rem aperiam, eaque ipsa quae ab illo inventore veritatis et quasi architecto beatae vitae dicta sunt explicabo. Nemo enim ipsam voluptatem quia voluptas sit aspernatur aut odit aut fugit.</p>
  <div class="btn btn-yellow" style="left:611px;top:271px;width:141px;height:32px">Get started now</div>
</section>

<div class="sec-title" style="top:972px">OUR SERVICES</div>
<div class="sec-sub" style="top:1010px">Sed ut perspiciatis unde omnis iste natus error sit voluptatem accusantium doloremque laudantium, totam rem aperiam, eaque ipsa quae ab illo inventore veritatis et quasi architecto beatae vitae dicta.</div>

<div class="service" style="left:160px">
  <div class="icon"><span><svg width="36" height="36" viewBox="0 0 36 36" fill="#fff"><rect x="4" y="12" width="5" height="12" rx="1"/><rect x="27" y="12" width="5" height="12" rx="1"/><rect x="9" y="16" width="18" height="4"/></svg></span></div>
  <h3 class="pink">BODY BUILDING</h3>
  <p>Sed ut perspiciatis unde omnis iste natus error sit voluptatem accusantium doloremque laudantium, totam rem aperiam, eaque ipsa quae ab illo inventore veritatis et quasi architecto beatae vitae dicta.</p>
  <div class="btn btn-pink" style="background:var(--pink-dark)">Read more</div>
</div>
<div class="service" style="left:461px">
  <div class="icon"><span><svg width="36" height="36" viewBox="0 0 36 36" fill="none" stroke="#fff" stroke-width="2.5"><path d="M12 6c3 6 3 18 0 24M24 6c-3 6-3 18 0 24"/><path d="M2 18h7M34 18h-7M6 15l3 3-3 3M30 15l-3 3 3 3"/></svg></span></div>
  <h3>WEIGHT LOSS</h3>
  <p>Sed ut perspiciatis unde omnis iste natus error sit voluptatem accusantium doloremque laudantium, totam rem aperiam, eaque ipsa quae ab illo inventore veritatis et quasi architecto beatae vitae dicta.</p>
  <div class="btn btn-pink">Read more</div>
</div>
<div class="service" style="left:760px">
  <div class="icon"><span><svg width="36" height="36" viewBox="0 0 36 36" fill="none" stroke="#fff" stroke-width="2.5"><circle cx="18" cy="20" r="11"/><path d="M18 20v-6M15 5h6M18 5v4"/></svg></span></div>
  <h3>FITNESS TRAINING</h3>
  <p>Sed ut perspiciatis unde omnis iste natus error sit voluptatem accusantium doloremque laudantium, totam rem aperiam, eaque ipsa quae ab illo inventore veritatis et quasi architecto beatae vitae dicta.</p>
  <div class="btn btn-pink">Read more</div>
</div>

<section class="stories" role="img" aria-label="Faded mosaic of client portrait photos">
  <div class="story-card">
    <h3>CLIENT SUCCESS STORIES</h3>
    <div class="avatar" role="img" aria-label="Client portrait"></div>
    <blockquote><b>"</b> Sed ut perspiciatis unde omnis iste natus error sit voluptatem accusantium doloremque laudantium, totam rem aperiam, eaque ipsa quae ab illo inventore veritatis et quasi architecto beatae vitae dicta sunt explicabo.</blockquote>
    <div class="who">John Doe</div>
    <div class="dots"><i class="on"></i><i></i><i></i><i></i></div>
  </div>
</section>

<div class="sec-title" style="top:1702px;font-size:17px">STAY UP TO DATE</div>

<div class="social chirp" style="left:160px">
  <div class="head"><i></i>Follow me on Chirper</div>
  <div class="pic" role="img" aria-label="Profile photo"></div>
  <div class="handle">TESSA ROWLE</div>
  <div class="rule"></div>
  <p><span>@tessarowle</span> Lorem Ipsum is simply dummy text of the printing and typesetting industry. Lorem Ipsum has been the industry's standard dummy text ever since the 1500s, when an unknown printer took.</p>
  <div class="foot"><span>◷ 2 days ago</span><u>View on chirper</u></div>
</div>
<div class="social friend" style="left:461px">
  <div class="head"><i></i>Like me on Friendbook</div>
  <div class="page" role="img" aria-label="Page photo"></div>
  <div class="pname">Tessa Rowle</div>
  <div class="like"></div>
  <div class="grid" role="img" aria-label="Grid of follower photos"><i></i><i></i><i></i><i></i><i></i><i></i><i></i><i></i><i></i><i></i><i></i></div>
  <div class="foot">friendbook social page</div>
</div>
<div class="social snap" style="left:760px">
  <div class="head"><i></i>Follow me on Snapgram</div>
  <div class="photo" role="img" aria-label="Two women flexing in a gym mirror selfie"></div>
  <div class="foot"><span style="color:var(--snap)">💬 10</span><span style="color:var(--snap)">♥ 90</span></div>
</div>

<div class="sec-title" style="top:2068px;font-size:17px">LATEST FROM BLOG</div>

<article class="post" style="left:160px">
  <div class="img" role="img" aria-label="Woman doing floor exercise" style="background:linear-gradient(135deg,#e1b37a,#8a5a3a)"></div>
  <h4>LOREM IPSUM IS SIMPLY DUMMY TEXT OF THE PRINTING AND TYPESETTING INDUSTRY.</h4>
  <p>Contrary to popular belief, Lorem Ipsum is not simply random text. It has roots in a piece of classical Latin literature from 45 BC, making it over 2000 years old. Daniel Harwick.</p>
  <a>Read more</a>
</article>
<article class="post" style="left:461px">
  <div class="img" role="img" aria-label="People training on gym machines" style="background:linear-gradient(135deg,#9fb2c2,#4e5e6c)"></div>
  <h4>LOREM IPSUM IS SIMPLY DUMMY TEXT OF THE PRINTING AND TYPESETTING INDUSTRY.</h4>
  <p>Contrary to popular belief, Lorem Ipsum is not simply random text. It has roots in a piece of classical Latin literature from 45 BC, making it over 2000 years old. Daniel Harwick.</p>
  <a>Read more</a>
</article>
<article class="post" style="left:760px">
  <div class="img" role="img" aria-label="Group working out on cardio bikes" style="background:linear-gradient(135deg,#c9a58a,#5c4537)"></div>
  <h4>LOREM IPSUM IS SIMPLY DUMMY TEXT OF THE PRINTING AND TYPESETTING INDUSTRY.</h4>
  <p>Contrary to popular belief, Lorem Ipsum is not simply random text. It has roots in a piece of classical Latin literature from 45 BC, making it over 2000 years old. Daniel Harwick.</p>
  <a>Read more</a>
</article>

<section class="cta">
  <h2>TESSA ROWLE FITNESS TRAINING</h2>
  <div class="sub">HELPS YOU GET MORE ACTIVE</div>
  <div class="btn btn-yellow">Get started now</div>
</section>

<footer class="footer">
  <div class="stay">STAY WITH ME</div>
  <div class="nets">
    <div class="net on"><i></i>friendbook</div>
    <div class="net"><i></i>chirper</div>
    <div class="net"><i></i>circles</div>
    <div class="net"><i></i>snapgram</div>
  </div>
  <div class="rule"></div>
  <div class="copy"><b>TESSAROWLE</b> © All reserved 2015.<br>Privacy &amp; Policy</div>
</footer>

</body>
</html>
```